One page clinic overview of clinic front and back info sheet

The Bio-Hacking Roadmap: A Lifetime of Optimization
1. The Foundation: Functional Diagnostics (The Discovery Phase)

Before any treatment, emphasize the "Data First" approach.

The Birdseye View: A header section titled "Your Biological Blueprint."

Content: Explain that every roadmap starts with Gut Microbiome Analysis, Comprehensive Hormone Panels, Dark Field Microscopy and Intracellular Nutrient Testing.

The Hook: "We don't guess; we test."

2. The 20s & 30s: Peak Performance & Preservation

Focus on high-energy lifestyles and preventing the onset of cellular aging.

Core Services: Targeted IM Shots (B12, CoQ10) for mitochondrial support and Nutritional IVs for recovery.

The Bio-Hack: Stress resilience and cycle syncing (for women) or testosterone optimization (for men).

3. The 40s: The Great Pivot (Hormonal Rebalancing)

Focus on the transition years where metabolism and hormones begin to shift.

Core Services: Hormone Optimization and Neural Therapy to reset the autonomic nervous system.

The Bio-Hack: Addressing "Inflammaging" at the root via gut health restoration.

4. The 50s+: Systemic Restoration & Longevity

Focus on "Turning back the clock" at a cellular level.

Core Services: Ozone Therapy, HHO/Brimtek therapy and Corvina Glowpulse Therapy

The Bio-Hack: Advanced cellular clean-up and vascular health optimization.

Strategic Service "Call-Out" Boxes
5. The "Neural Therapy" Reset

A dedicated sidebar explaining that this isn't just an injection; it's a "reboot" for your nervous system's electrical interference, helping with chronic pain and energetic blocks.
6. Enhanced OZONE IV and Injection Therapy
A visual call-out for Ozone therapy. It works on the cells and causes a disruption of the natural replication process of harmful invaders to your body. Ozone therapy can inactivate: Bacteria, Viruses, Fungi, Yeast, Protozoa. In fact, IV ozone treatment benefits most immune diseases.

7. The Nutrient Infusion Menu (IV vs. IM)

A simple comparison chart:

IM Shots: 5-minute cellular boosts (The "Quick Charge").

Nutritional IVs: Deep systemic saturation for hydration and 100% bioavailability.

The "Personalization" Elements
8. The "Bio-Individual" Legend

A small infographic showing how one client’s "Energy" IV is different from another’s based on their blood work. Use icons for Gut, Brain, and Heart.
9. The "Continuous Feedback Loop"

A section at the bottom of the page showing a circular arrow: Test → Treat → Track. This reinforces that their "roadmap" evolves as their biomarkers improve.
10. The Concierge Call-to-Action

"Your biology is unique; your treatment should be too." Include a QR code labeled: "Book Your Diagnostic Consultation."
Example Layout for the 8.5x11" Sheet
Section Visual Element Key Message
Top Header Modern, clean logo + "The Longevity Roadmap" Personalized Bio-Hacking
Middle Left Age 20–40: Performance & Defense IV/IM + Gut Health
Middle Right Age 40–60+: Restoration & Revitalization Hormones + Plasma + Ozone + Brimtek therapy
Bottom Bar Icons for Gut, Hormone, and Nutrient Testing "Driven by your data."

medical wellness clinic

Sans Serif
Script

0094D4
00A9DD
6FCCEA
C7EBF8
E9F6FB
00AB8E
00BBA5
67D7C9
C6EFE9
E9F9F6
6B429C
8869AF
B7A5CE
E3DAEB
F3F0F8

• Please draw from the uploaded one page sheet for additional ideas

```html
<!DOCTYPE html>
<html lang="en">
<head>
<meta charset="utf-8">
<title>The Longevity Roadmap – Verdalis MD</title>
<link href="https://fonts.googleapis.com/css2?family=Oswald:wght@300;600;700&family=Poppins:wght@400;500;600;700&display=swap" rel="stylesheet">
<style>
:root{
  --page:#d3d3d3;
  --paper:#ffffff;
  --green-dark:#4f8a3a;
  --green:#6a9a2a;
  --lime:#b6d23f;
  --lime-soft:#dbe9a6;
  --tint:#e1e8d4;
  --bar:#ececec;
  --ink:#2b3a3f;
  --text:#333333;
}
*{box-sizing:border-box;margin:0;padding:0}
html,body{width:962px;height:1200px;overflow:hidden;background:var(--page)}
body{font-family:"Poppins",sans-serif;color:var(--text)}
.sheet{position:absolute;left:58px;top:53px;width:845px;height:1094px;background:var(--paper);overflow:hidden}
.abs{position:absolute}
.header-wave{left:0;top:0;width:845px;height:180px}
.brand{left:47px;top:34px;color:#fff}
.brand-name{display:flex;align-items:center;gap:10px;font-weight:600;font-size:42px;line-height:1}
.brand-dot{width:44px;height:44px;border-radius:50%;background:#fff;opacity:.9}
.brand-tag{margin:12px 0 0 54px;font-size:12.5px;letter-spacing:2.4px;font-weight:400}
.brand-url{margin:4px 0 0 54px;font-size:15px;font-weight:400}
.hero-art{left:570px;top:62px;width:225px;height:265px;border-radius:40% 40% 20% 20%;background:linear-gradient(160deg,#e6efe3,#b9d9b6 55%,#6aa85a)}
.title{left:47px;top:192px;font-family:"Oswald",sans-serif;font-weight:700;font-size:49px;line-height:1;color:var(--ink);letter-spacing:.5px}
.subtitle{left:47px;top:246px;font-weight:700;font-size:36px;color:#8cb63c;line-height:1.1}
.tagline{left:47px;top:294px;font-weight:600;font-size:20px;color:#1e1e1e;display:flex;align-items:center;gap:12px}
.tagline::after{content:"";width:88px;height:1px;background:#333}
.blueprint-band{left:0;top:352px;width:845px;height:69px;background:linear-gradient(90deg,var(--green-dark),#8cb63c 60%,var(--lime) 85%,var(--green-dark))}
.blueprint-title{left:47px;top:365px;font-weight:700;font-size:30px;color:#fff}
.test-tab{left:464px;top:368px;width:381px;height:50px;background:#fff;border-radius:40px 0 0 0;display:flex;align-items:center;gap:10px;padding-left:40px;font-weight:700;font-size:19px;color:var(--ink)}
.starts{left:45px;top:436px;font-weight:600;font-size:18px;color:#1e1e1e;display:flex;align-items:center;gap:6px}
.starts::after{content:"";width:118px;height:1px;background:#333}
.test-item{top:476px;display:flex;align-items:center;gap:14px}
.test-item svg{width:50px;height:50px;flex:none}
.test-item span{font-weight:700;font-size:15px;line-height:1.18;color:var(--green)}
.divider{left:0;top:573px;width:845px;height:3px;background:var(--green-dark)}
.stage{top:579px;width:277px}
.stage-head{height:111px;background:var(--tint);text-align:center;padding-top:17px}
.stage-head h2{font-weight:700;font-size:28px;color:var(--ink);line-height:1.1}
.stage-head p{margin-top:6px;font-weight:600;font-size:14.5px;line-height:1.25;color:var(--green)}
.bar{position:absolute;left:0;width:277px;height:24px;background:var(--bar);display:flex;align-items:center;gap:10px;padding-left:50px;font-weight:700;font-size:17px;color:var(--green)}
.bar svg{position:absolute;left:50px;width:18px;height:18px}
.bar b{margin-left:28px}
.body{position:absolute;left:45px;width:225px;font-size:10px;line-height:1.65;color:#222}
.list{position:absolute;left:45px;width:225px;list-style:none;font-size:10px;line-height:1.3;color:#222}
.list li{position:relative;padding-left:13px;margin-bottom:5px}
.list li::before{content:"";position:absolute;left:0;top:4px;width:4px;height:4px;border-radius:50%;background:var(--green)}
.list.hack li{margin-bottom:3px}
.list.hack li::before{width:5px;height:4px;border-radius:0 4px 0 4px}
.footer-band{left:0;top:992px;width:845px;height:102px;background:linear-gradient(90deg,var(--lime),#8cb63c 55%,var(--green-dark))}
.footer-line{left:0;top:992px;width:500px;height:4px;background:var(--green-dark)}
.footer-tab{left:0;top:998px;width:495px;height:96px;background:#fff;border-radius:0 22px 0 0}
.driven{left:45px;top:1016px;font-family:"Oswald",sans-serif;font-size:52px;line-height:1;color:var(--ink)}
.driven .light{font-weight:300}
.driven .bold{font-weight:700}
.pillar{top:958px;width:90px;text-align:center;color:#fff;font-family:"Oswald",sans-serif;font-weight:600;font-size:21px;line-height:1.05}
.pillar-circle{width:66px;height:66px;margin:0 auto 11px;border-radius:50%;background:#fff;border:2px solid var(--green-dark);display:flex;align-items:center;justify-content:center}
.pillar-circle svg{width:38px;height:38px}
.pillar.small{font-size:17px}
</style>
</head>
<body>
<main class="sheet">

  <svg class="abs header-wave" viewBox="0 0 845 180" preserveAspectRatio="none" aria-hidden="true">
    <defs>
      <linearGradient id="hdr" x1="0" x2="1">
        <stop offset="0" stop-color="#4f8a3a"/><stop offset=".6" stop-color="#86b43e"/><stop offset="1" stop-color="#b6d23f"/>
      </linearGradient>
      <linearGradient id="lm" x1="0" x2="1">
        <stop offset="0" stop-color="#b6d23f"/><stop offset=".5" stop-color="#e4efbf"/><stop offset="1" stop-color="#ffffff"/>
      </linearGradient>
    </defs>
    <path d="M0 125 C160 175 330 175 480 120 S740 40 845 50 V0 H0Z" fill="url(#lm)"/>
    <path d="M0 0 H845 V50 C740 30 600 60 470 100 S160 160 0 118Z" fill="url(#hdr)"/>
  </svg>

  <div class="abs brand">
    <div class="brand-name"><span class="brand-dot"></span>Verdalis MD</div>
    <div class="brand-tag">VITALITY • STRENGTH • LONGEVITY</div>
    <div class="brand-url">verdalismd.com</div>
  </div>

  <div class="abs hero-art" role="img" aria-label="Illustration of a clinician in a lab coat beside a green DNA helix and foliage"></div>

  <h1 class="abs title">THE LONGEVITY ROADMAP</h1>
  <p class="abs subtitle">Personalized Bio-hacking</p>
  <p class="abs tagline">For A Lifetime Of Optimization</p>

  <div class="abs blueprint-band"></div>
  <h2 class="abs blueprint-title">Your Biological Blueprint</h2>
  <div class="abs test-tab">
    <svg width="26" height="30" viewBox="0 0 26 30" fill="none" stroke="#2b3a3f" stroke-width="2"><path d="M4 2h15l4 4v10M4 2v26h10"/><path d="M8 9h11M8 14h11M8 19h6"/><path d="M15 24l3 3 6-7"/></svg>
    WE DON'T GUESS; WE TEST
  </div>

  <p class="abs starts">Every Roadmap Starts With :</p>

  <div class="abs test-item" style="left:47px">
    <svg viewBox="0 0 50 50" fill="none" stroke="#6a9a2a" stroke-width="2.2"><path d="M8 40V12c0-5 6-6 8-2 2-4 10-4 12 0 3-3 8-1 8 3v8M8 26h14"/><circle cx="34" cy="36" r="10"/><circle cx="31" cy="33" r="2"/><circle cx="37" cy="38" r="2"/></svg>
    <span>Gut<br>Microbiome<br>Analysis</span>
  </div>
  <div class="abs test-item" style="left:240px">
    <svg viewBox="0 0 50 50" fill="none" stroke="#6a9a2a" stroke-width="2.2"><path d="M4 20h9v22a4.5 4.5 0 01-9 0zM16 20h9v22a4.5 4.5 0 01-9 0zM28 26h8v16a4 4 0 01-8 0z"/><circle cx="34" cy="12" r="9"/><path d="M40 18l7 7"/></svg>
    <span>Comprehensive<br>Hormone<br>Panels</span>
  </div>
  <div class="abs test-item" style="left:458px">
    <svg viewBox="0 0 50 50" fill="none" stroke="#6a9a2a" stroke-width="2.2"><path d="M18 4l10 6-8 14-10-6zM22 24l-2 8M6 44h38M10 44c0-10 6-16 14-16M28 36h12v8"/><circle cx="24" cy="18" r="3"/></svg>
    <span>Dark<br>Field<br>Microscopy</span>
  </div>
  <div class="abs test-item" style="left:645px">
    <svg viewBox="0 0 50 50" fill="none" stroke="#6a9a2a" stroke-width="2.2"><circle cx="25" cy="16" r="11"/><path d="M25 46C14 46 5 38 5 26c10 0 20 8 20 20zM25 46c11 0 20-8 20-20-10 0-20 8-20 20zM18 38l7 8 7-8"/></svg>
    <span>Intracellular<br>Nutrient<br>Testing</span>
  </div>

  <div class="abs divider"></div>

  <section class="abs stage" style="left:0">
    <div class="stage-head"><h2>THE 20S &amp; 30S</h2><p>Peak Performance &amp;<br>Preservation</p></div>
  </section>
  <section class="abs stage" style="left:284px">
    <div class="stage-head"><h2>THE 40s</h2><p>The Great Pivot<br>(Hormonal Rebalancing)</p></div>
  </section>
  <section class="abs stage" style="left:568px">
    <div class="stage-head"><h2>THE 50s</h2><p>Systemic Restoration<br>&amp; Longevity</p></div>
  </section>

  <!-- column: 20s & 30s -->
  <div class="abs" style="left:0;top:0;width:277px">
    <div class="bar" style="top:709px"><svg viewBox="0 0 18 18" fill="none" stroke="#6a9a2a" stroke-width="2"><circle cx="9" cy="9" r="7.5"/><circle cx="9" cy="9" r="3.5"/><path d="M9 9l7-7"/></svg><b>Focus On</b></div>
    <p class="body" style="top:742px">High-energy Lifestyles And Preventing The Onset Of Cellular Aging</p>
    <div class="bar" style="top:789px"><svg viewBox="0 0 18 18" fill="#6a9a2a"><path d="M7.5 0h3l.5 3 2 1 2.5-2 2 2-2 2.5 1 2 3 .5v3l-3 .5-1 2 2 2.5-2 2-2.5-2-2 1-.5 3h-3l-.5-3-2-1-2.5 2-2-2 2-2.5-1-2-3-.5v-3l3-.5 1-2-2-2.5 2-2 2.5 2 2-1zM9 6a3 3 0 100 6 3 3 0 000-6z"/></svg><b>Core Services</b></div>
    <ul class="list" style="top:828px"><li>Targeted Im Shots (B12, Coq10) For Mitochondrial Support</li><li>Nutritional Ivs For Recovery</li></ul>
    <div class="bar" style="top:886px"><svg viewBox="0 0 18 18" fill="none" stroke="#6a9a2a" stroke-width="1.6"><path d="M2 16C6 12 12 6 16 2M2 10c4 0 6 2 6 6M10 2c0 4 2 6 6 6"/></svg><b>The Bio-Hack</b></div>
    <ul class="list hack" style="top:924px"><li>Stress resilience</li><li>Cycle syncing (for women)</li><li>Testosterone optimization (for men)</li></ul>
  </div>

  <!-- column: 40s -->
  <div class="abs" style="left:284px;top:0;width:277px">
    <div class="bar" style="top:709px"><svg viewBox="0 0 18 18" fill="none" stroke="#6a9a2a" stroke-width="2"><circle cx="9" cy="9" r="7.5"/><circle cx="9" cy="9" r="3.5"/><path d="M9 9l7-7"/></svg><b>Focus On</b></div>
    <p class="body" style="top:742px">Transition years where metabolism &amp; hormones begin to shift.</p>
    <div class="bar" style="top:789px"><svg viewBox="0 0 18 18" fill="#6a9a2a"><path d="M7.5 0h3l.5 3 2 1 2.5-2 2 2-2 2.5 1 2 3 .5v3l-3 .5-1 2 2 2.5-2 2-2.5-2-2 1-.5 3h-3l-.5-3-2-1-2.5 2-2-2 2-2.5-1-2-3-.5v-3l3-.5 1-2-2-2.5 2-2 2.5 2 2-1zM9 6a3 3 0 100 6 3 3 0 000-6z"/></svg><b>Core Services</b></div>
    <ul class="list" style="top:828px;width:205px"><li>Hormone Optimization</li><li>Neural Therapy to reset the autonomic nervous system</li></ul>
    <div class="bar" style="top:886px"><svg viewBox="0 0 18 18" fill="none" stroke="#6a9a2a" stroke-width="1.6"><path d="M2 16C6 12 12 6 16 2M2 10c4 0 6 2 6 6M10 2c0 4 2 6 6 6"/></svg><b>The Bio-Hack</b></div>
    <ul class="list hack" style="top:924px;width:200px"><li>Addressing “Inflammaging” at the root via gut health restoration</li></ul>
  </div>

  <!-- column: 50s -->
  <div class="abs" style="left:568px;top:0;width:277px">
    <div class="bar" style="top:709px"><svg viewBox="0 0 18 18" fill="none" stroke="#6a9a2a" stroke-width="2"><circle cx="9" cy="9" r="7.5"/><circle cx="9" cy="9" r="3.5"/><path d="M9 9l7-7"/></svg><b>Focus On</b></div>
    <p class="body" style="top:742px">Turning back the clock at a cellular level.</p>
    <div class="bar" style="top:789px"><svg viewBox="0 0 18 18" fill="#6a9a2a"><path d="M7.5 0h3l.5 3 2 1 2.5-2 2 2-2 2.5 1 2 3 .5v3l-3 .5-1 2 2 2.5-2 2-2.5-2-2 1-.5 3h-3l-.5-3-2-1-2.5 2-2-2 2-2.5-1-2-3-.5v-3l3-.5 1-2-2-2.5 2-2 2.5 2 2-1zM9 6a3 3 0 100 6 3 3 0 000-6z"/></svg><b>Core Services</b></div>
    <ul class="list" style="top:828px"><li style="margin-bottom:3px">Ozone Therapy</li><li style="margin-bottom:3px">HHO / Brimtek Therapy</li><li>Corvina Glowpulse Therapy</li></ul>
    <div class="bar" style="top:886px"><svg viewBox="0 0 18 18" fill="none" stroke="#6a9a2a" stroke-width="1.6"><path d="M2 16C6 12 12 6 16 2M2 10c4 0 6 2 6 6M10 2c0 4 2 6 6 6"/></svg><b>The Bio-Hack</b></div>
    <ul class="list hack" style="top:924px"><li>Advanced cellular clean-up</li><li>Vascular health optimization</li></ul>
  </div>

  <div class="abs footer-band"></div>
  <div class="abs footer-line"></div>
  <div class="abs footer-tab"></div>
  <p class="abs driven"><span class="light">DRIVEN</span> <span class="bold">BY YOUR DATA</span></p>

  <div class="abs pillar" style="left:503px">
    <div class="pillar-circle"><svg viewBox="0 0 38 38" fill="none" stroke="#6a9a2a" stroke-width="2"><path d="M19 2v6c-8 0-10 3-10 5s3 4 10 4 10 2 10 4-3 4-10 4-10 2-10 4 3 4 10 4v3"/></svg></div>
    GUT
  </div>
  <div class="abs pillar" style="left:609px">
    <div class="pillar-circle"><svg viewBox="0 0 38 38" fill="none" stroke="#6a9a2a" stroke-width="2"><path d="M8 20l6-4 6 4v7l-6 4-6-4zM20 20l6-4 6 4M26 16V9l5-3M8 23H3"/><circle cx="31" cy="6" r="2"/><circle cx="3" cy="23" r="2"/></svg></div>
    HORMONE
  </div>
  <div class="abs pillar small" style="left:719px">
    <div class="pillar-circle"><svg viewBox="0 0 38 38" fill="none" stroke="#6a9a2a" stroke-width="2"><path d="M14 12h10M16 12v8L8 34h22l-8-14v-8M19 10c0-4 3-6 6-6-1 3-3 5-6 6zM19 10c0-3-2-5-5-5 0 3 2 5 5 5z"/><circle cx="16" cy="29" r="1.5"/><circle cx="22" cy="29" r="1.5"/><circle cx="19" cy="25" r="1.5"/></svg></div>
    NUTRIENT<br>TESTING
  </div>

</main>
</body>
</html>
```